Business Card Design

we sell natural, organic & biological products. our brand includes verdalune - hair dye products, morvesa-baby skin care and toothpaste... all products from Italy. our target customers are pharmacies, organic shops & stores, mum and baby care shops,.. i would love to see designs that use natural color, simple, friendly, eco concept.
Il Campo Vesco is Italian language, means Quiet meadow, referring to the best parts on the top of wheat. The brands we carried currently are VerdaLune Piana and Morvesa.

Target Market(s)

organic shops & store, pharmacies, mum n baby shops, bio/organic product users

Industry/Entity Type

Hair

Contact Information for Business Card

Mabel Khoo WeiTing
Sales Manager
Il Campo Vesco Singapore
Blk 318 Pinecrest Avenue7
#07-12 Singapore 648271
Tel +65 6173 4820 Mobile +65 87460395
Reg No 48207315K
www.facebook.com/ilcampovescosg

Requirements
Must have
• The front of the card should have my name, followed by my job title, my email address. Then the office address (company reg no), office tel, mobile phone.

My namecard should have all the brands my company carries.
Like ‘Morvesa’, ‘Verdalune piana’. Should have the brand logos too. This should be stated clearly at the back of the card. I will upload 'Verdalune' logo once I have it.

```html
<!DOCTYPE html>
<html lang="en">
<head>
<meta charset="utf-8">
<title>Il Campo Vesco – Business Card</title>
<link rel="stylesheet" href="https://fonts.googleapis.com/css2?family=Michroma&display=swap">
<style>
  :root {
    --bg: #e9ecee;
    --card: #ffffff;
    --card-shade: #f1f2f3;
    --blue: #00aeef;
    --green: #8cc63f;
    --white: #ffffff;
  }
  * { box-sizing: border-box; margin: 0; padding: 0; }
  html, body {
    width: 1200px; height: 898px; overflow: hidden;
    background: var(--bg);
    font-family: "Michroma", "Arial", sans-serif;
  }
  .stage {
    width: 1200px; height: 898px;
    display: flex; align-items: center; justify-content: center; gap: 40px;
  }
  .card {
    width: 540px; height: 310px;
    background: linear-gradient(135deg, var(--card) 0%, var(--card-shade) 100%);
    position: relative; overflow: hidden;
    box-shadow: 0 6px 18px rgba(0,0,0,.12);
  }
  .brand {
    display: flex; flex-direction: column; align-items: center; gap: 12px;
  }
  .brand-dot {
    width: 54px; height: 54px; border-radius: 50%;
    border: 4px solid var(--green);
  }
  .brand-name {
    color: var(--blue); font-size: 22px; letter-spacing: 1px; white-space: nowrap;
  }
  .brand-lines {
    color: var(--blue); font-size: 9px; letter-spacing: 1px; white-space: nowrap;
  }
  .card-front { display: flex; align-items: center; justify-content: center; }

  .card-back { display: flex; }
  .edge-stripe {
    position: absolute; left: 0; top: 0; width: 9px; height: 100%;
    background: linear-gradient(var(--blue) 0 38%, var(--green) 38% 68%, var(--blue) 68% 100%);
  }
  .back-brand {
    width: 280px; display: flex; align-items: center; justify-content: center; padding-left: 9px;
  }
  .back-brand .brand-dot { width: 40px; height: 40px; border-width: 3px; }
  .back-brand .brand-name { font-size: 15px; }
  .contact-panel {
    width: 260px; height: 100%; background: var(--blue); color: var(--white);
    padding: 22px 16px; text-align: right;
    display: flex; flex-direction: column;
  }
  .person-name { font-size: 13px; letter-spacing: 0.5px; white-space: nowrap; }
  .person-role { font-size: 8.5px; letter-spacing: 1px; margin-top: 5px; }
  .address { font-size: 8.5px; line-height: 1.7; margin-top: 26px; white-space: nowrap; }
  .contact-list { list-style: none; margin-top: 18px; font-size: 8px; line-height: 2; }
  .contact-list li { display: flex; justify-content: flex-end; align-items: center; gap: 7px; white-space: nowrap; }
  .contact-list svg { width: 10px; height: 10px; fill: var(--white); flex: none; }
</style>
</head>
<body>
<main class="stage">
  <section class="card card-front">
    <div class="brand">
      <span class="brand-dot"></span>
      <span class="brand-name">Il Campo Vesco</span>
      <span class="brand-lines">Morvesa · VerdaLune Piana</span>
    </div>
  </section>

  <section class="card card-back">
    <span class="edge-stripe"></span>
    <div class="back-brand">
      <div class="brand">
        <span class="brand-dot"></span>
        <span class="brand-name">Il Campo Vesco</span>
      </div>
    </div>
    <div class="contact-panel">
      <p class="person-name">MABEL KHOO WEITING</p>
      <p class="person-role">SALES MANAGER</p>
      <p class="address">Blk 318 Pinecrest Avenue7<br>#07-12 Singapore 648271<br>Reg No 48207315K</p>
      <ul class="contact-list">
        <li>+65 6173 4820
          <svg viewBox="0 0 24 24"><path d="M6.6 10.8a15 15 0 0 0 6.6 6.6l2.2-2.2c.3-.3.7-.4 1-.2 1.1.4 2.3.6 3.6.6.6 0 1 .4 1 1V20c0 .6-.4 1-1 1A17 17 0 0 1 3 4c0-.6.4-1 1-1h3.5c.6 0 1 .4 1 1 0 1.3.2 2.5.6 3.6.1.3 0 .7-.2 1z"/></svg></li>
        <li>+65 87460395
          <svg viewBox="0 0 24 24"><path d="M7 1h10a2 2 0 0 1 2 2v18a2 2 0 0 1-2 2H7a2 2 0 0 1-2-2V3a2 2 0 0 1 2-2zm0 3v14h10V4zm5 15.5a1 1 0 1 0 0 2 1 1 0 0 0 0-2z"/></svg></li>
        <li>sales@ilcampovesco.sg
          <svg viewBox="0 0 24 24"><path d="M2 5h20v14H2zm2 2v.5l8 5 8-5V7zm0 3v7h16v-7l-8 5z"/></svg></li>
        <li>www.facebook.com/ilcampovescosg
          <svg viewBox="0 0 24 24"><path d="M12 2a10 10 0 1 0 0 20 10 10 0 0 0 0-20zm6.9 9h-3a15 15 0 0 0-1.3-5.6A8 8 0 0 1 18.9 11zM12 4c.9 1.2 1.8 3.6 1.9 7h-3.8c.1-3.4 1-5.8 1.9-7zM9.4 5.4A15 15 0 0 0 8.1 11h-3a8 8 0 0 1 4.3-5.6zM5.1 13h3a15 15 0 0 0 1.3 5.6A8 8 0 0 1 5.1 13zm6.9 7c-.9-1.2-1.8-3.6-1.9-7h3.8c-.1 3.4-1 5.8-1.9 7zm2.6-1.4a15 15 0 0 0 1.3-5.6h3a8 8 0 0 1-4.3 5.6z"/></svg></li>
      </ul>
    </div>
  </section>
</main>
</body>
</html>
```